Flyer design wanted for whole-body cold therapy/cryotherapy in the sports sector (dr...

We operate a cryo sauna in a health center and are currently primarily geared towards the medical field (pain therapy). In order to address the other target group of athletes in terms of performance increase and regeneration, we would like a clean and dynamic design, preferably with contrasting colors. Our company colors are currently kept in a light and dark shade of green. We are currently working with the fonts Montserrat and Sansation. The overall impression of the folder should harmonize with this, but we are completely open to color and font suggestions. Information about us can be found at velmarin.at. Should you require any further information, please contact us.

```html
<!DOCTYPE html>
<html lang="de">
<head>
<meta charset="utf-8">
<title>Velmarin – Kältetherapie Folder</title>
<link href="https://fonts.googleapis.com/css2?family=Montserrat:ital,wght@0,300;0,400;0,500;0,600;0,700;1,300&display=swap" rel="stylesheet">
<style>
:root{
  --navy:#1f2a38;
  --navy-2:#2a3747;
  --teal:#5e8d8a;
  --teal-light:#9dbdba;
  --teal-pale:#d9e7e5;
  --white:#ffffff;
  --page:#eceeef;
  --muted:#c9d3dc;
  --ice:#b9cfdc;
}
*{margin:0;padding:0;box-sizing:border-box}
html,body{width:831px;height:1200px;overflow:hidden;background:var(--page)}
body{font-family:"Montserrat",sans-serif;color:var(--navy);position:relative}
.spread{position:absolute;left:30px;width:771px;height:552px;display:flex;box-shadow:0 3px 10px rgba(0,0,0,.18)}
.spread--outside{top:30px}
.spread--inside{top:618px}
.panel{position:relative;width:257px;height:100%;overflow:hidden}
.photo{position:absolute}
.dark{background:var(--navy);color:var(--white)}
.light{background:var(--white)}
.heading{font-size:9px;font-weight:700;letter-spacing:.06em;text-transform:uppercase;line-height:1.3}
.copy{font-size:5.6px;line-height:1.55;font-weight:400}
.copy p+p{margin-top:5px}
.brand{font-weight:600;letter-spacing:.03em}
.brand-mark{display:inline-block;width:9px;height:9px;border-radius:50%;background:currentColor;margin-right:5px;vertical-align:middle}
.list-item{display:flex;gap:8px;margin-bottom:9px;align-items:flex-start}
.list-icon{flex:0 0 18px;height:18px;border-radius:50%;border:1.2px solid var(--teal-light);display:flex;align-items:center;justify-content:center}
.list-title{font-size:6px;font-weight:700;color:var(--teal-light);text-transform:uppercase;margin-bottom:2px}
.price-row{display:flex;justify-content:space-between;font-size:5.6px;padding:4px 0;border-bottom:.6px solid rgba(255,255,255,.2)}
.price-row b{color:var(--teal-light);font-weight:600}
</style>
</head>
<body>

<!-- OUTSIDE -->
<section class="spread spread--outside">
  <!-- inner flap -->
  <div class="panel dark">
    <div style="position:absolute;left:22px;top:26px;width:212px">
      <h2 class="heading" style="color:var(--teal-light)">Kältetherapie mit<br>Ganzkörperwirkung</h2>
      <div class="copy" style="margin-top:10px;color:var(--muted)">
        <p>In der Kältesauna wird der gesamte Körper für wenige Minuten trockener Kälte ausgesetzt. Die Haut kühlt rasch ab, während die Körperkerntemperatur stabil bleibt. So entsteht ein starker Reiz für Kreislauf, Stoffwechsel und Nervensystem.</p>
        <p>Die Anwendung ist kurz, angenehm trocken und gut verträglich. Viele Gäste berichten von spürbarer Frische, mehr Energie und einem klaren Kopf direkt nach der Behandlung.</p>
        <p>Der Kältereiz regt die Durchblutung an, unterstützt die Regeneration nach Belastung und kann Entzündungsprozesse sowie Schmerzen im Bewegungsapparat lindern.</p>
        <p>Für Sportler bedeutet das kürzere Erholungszeiten, weniger Muskelkater und eine bessere Vorbereitung auf die nächste Einheit oder den Wettkampf.</p>
        <p>Unser geschultes Team begleitet Sie bei jeder Anwendung und stimmt die Dauer individuell auf Ihr Ziel und Ihre Verfassung ab.</p>
      </div>
    </div>
    <div class="photo" role="img" aria-label="Foto: Mann in der Kältesauna" style="left:22px;top:368px;width:100px;height:160px;background:linear-gradient(160deg,#8aa0b3,#3a4a5c)"></div>
    <div class="photo" role="img" aria-label="Foto: Läufer in Startposition auf Eis" style="left:128px;top:368px;width:108px;height:160px;background:linear-gradient(200deg,#c8d6e0,#6d7f90 60%,#9b3b2e)"></div>
  </div>

  <!-- back panel -->
  <div class="panel light">
    <svg style="position:absolute;left:0;top:0" width="257" height="552" viewBox="0 0 257 552">
      <path d="M0 150 C80 130 180 170 257 140 L257 300 C180 320 80 290 0 310 Z" fill="var(--teal)"/>
      <path d="M0 300 C90 285 170 320 257 300 L257 315 C170 332 90 300 0 318 Z" fill="var(--teal-light)"/>
    </svg>
    <div style="position:absolute;left:0;right:0;top:52px;text-align:center;color:var(--teal);font-size:15px" class="brand"><span class="brand-mark"></span>Velmarin</div>
    <div style="position:absolute;left:0;right:0;top:178px;text-align:center;color:var(--white)">
      <div class="heading" style="font-size:8px">Kurbehandlung<br>mit Langzeitwirkung</div>
      <div class="copy" style="margin:8px auto 0;width:190px">Zehn Anwendungen innerhalb weniger Wochen verstärken den Effekt nachhaltig und fördern die Anpassung des Körpers an den Kältereiz.</div>
      <div style="margin-top:12px;font-size:6.5px;font-weight:700;letter-spacing:.04em">SONDERPREIS 10ER-KARTE € 390,–</div>
    </div>
    <div style="position:absolute;left:26px;right:26px;top:340px;text-align:center" class="copy">
      <p>Vereinbaren Sie Ihren Termin telefonisch oder per E-Mail. Gutscheine sind vor Ort erhältlich.</p>
      <p style="margin-top:10px;color:var(--teal);font-weight:600">Ihr Zentrum für Gesundheit &amp; Regeneration</p>
    </div>
    <div style="position:absolute;left:0;right:0;top:430px;text-align:center;font-size:6px;line-height:1.7">
      Lindenweg 12 · 4020 Talheim<br>T +43 123 456 789<br>office@velmarin.at
    </div>
  </div>

  <!-- front cover -->
  <div class="panel dark">
    <div class="photo" role="img" aria-label="Foto: Läufer in roter Jacke in Eislandschaft" style="left:0;top:0;width:257px;height:420px;background:linear-gradient(175deg,#dfe8ee 0%,#a9bfce 45%,#6f8799 80%,#3e5062 100%)"></div>
    <div style="position:absolute;right:16px;top:22px;text-align:right;color:var(--navy)">
      <div style="font-size:11px;font-weight:300;font-style:italic">Wohlbefinden…</div>
      <div style="font-size:11px;font-weight:300;font-style:italic;margin-top:2px">mit der Kraft der Kälte</div>
      <div style="font-size:5px;font-weight:600;margin-top:4px;letter-spacing:.05em">NUR 3 MINUTEN BEI −110 °C</div>
    </div>
    <svg style="position:absolute;left:0;top:380px" width="257" height="172" viewBox="0 0 257 172">
      <path d="M0 20 C90 60 170 10 257 30 L257 172 L0 172 Z" fill="var(--teal-light)"/>
      <path d="M0 32 C90 72 170 22 257 42 L257 172 L0 172 Z" fill="var(--navy)"/>
    </svg>
    <div style="position:absolute;left:0;right:0;top:470px;text-align:center;color:var(--teal-light);font-size:16px" class="brand"><span class="brand-mark"></span>Velmarin</div>
    <div style="position:absolute;right:18px;bottom:14px;font-size:7px;font-weight:600;letter-spacing:.05em">www.velmarin.at</div>
  </div>
</section>

<!-- INSIDE -->
<section class="spread spread--inside">
  <div class="panel light">
    <div class="photo" role="img" aria-label="Foto: Kältesauna-Kabine" style="left:0;top:0;width:257px;height:250px;background:linear-gradient(180deg,#c7ced4,#5a6570 70%,#2e3742)"></div>
    <svg style="position:absolute;left:0;top:215px" width="257" height="60" viewBox="0 0 257 60">
      <path d="M0 30 C80 0 170 50 257 20 L257 60 L0 60 Z" fill="var(--white)"/>
    </svg>
    <div style="position:absolute;left:22px;top:272px;width:212px">
      <h2 style="font-size:11px;font-weight:600;color:var(--teal)">Die Cryo Sauna</h2>
      <div class="copy" style="margin-top:8px">
        <p>Die Cryo Sauna ist eine Kältekammer für eine Person. Der Kopf bleibt außerhalb, sodass Sie frei atmen und sich jederzeit mit unserem Personal unterhalten können.</p>
        <p>Trockener, gekühlter Stickstoff umströmt den Körper und senkt die Hauttemperatur innerhalb kurzer Zeit deutlich ab. Eine Anwendung dauert nur zwei bis drei Minuten.</p>
        <p>Nach der Behandlung erwärmt sich der Körper von selbst. Die verstärkte Durchblutung sorgt für ein wohliges Gefühl und neue Energie.</p>
        <p>Die Behandlung ist sicher, hygienisch und wird stets individuell auf Sie abgestimmt.</p>
      </div>
    </div>
    <div style="position:absolute;left:0;right:0;bottom:14px;text-align:center;font-size:6.5px;font-weight:600;color:var(--teal)">www.velmarin.at</div>
  </div>

  <div class="panel dark" style="background:var(--navy-2)">
    <div style="position:absolute;left:22px;top:26px;width:212px">
      <h2 class="heading" style="text-align:center;color:var(--teal-light);margin-bottom:14px">Was ist möglich?</h2>
      <div class="list-item"><span class="list-icon"><svg width="8" height="8" viewBox="0 0 8 8"><path d="M1 4l2 2 4-4" stroke="#9dbdba" fill="none" stroke-width="1.2"/></svg></span><div><div class="list-title">Schmerzlinderung</div><div class="copy" style="color:var(--muted)">Bei Gelenk- und Rückenbeschwerden sowie entzündlichen Prozessen.</div></div></div>
      <div class="list-item"><span class="list-icon"><svg width="8" height="8" viewBox="0 0 8 8"><path d="M1 4l2 2 4-4" stroke="#9dbdba" fill="none" stroke-width="1.2"/></svg></span><div><div class="list-title">Regeneration</div><div class="copy" style="color:var(--muted)">Schnellere Erholung nach Training und Wettkampf, weniger Muskelkater.</div></div></div>
      <div class="list-item"><span class="list-icon"><svg width="8" height="8" viewBox="0 0 8 8"><path d="M1 4l2 2 4-4" stroke="#9dbdba" fill="none" stroke-width="1.2"/></svg></span><div><div class="list-title">Leistungssteigerung</div><div class="copy" style="color:var(--muted)">Mehr Energie, bessere Belastbarkeit und gesteigerte Konzentration.</div></div></div>
      <div class="list-item"><span class="list-icon"><svg width="8" height="8" viewBox="0 0 8 8"><path d="M1 4l2 2 4-4" stroke="#9dbdba" fill="none" stroke-width="1.2"/></svg></span><div><div class="list-title">Beauty &amp; Wellness</div><div class="copy" style="color:var(--muted)">Straffere Haut und ein frisches, gesundes Hautbild.</div></div></div>
      <div class="list-item"><span class="list-icon"><svg width="8" height="8" viewBox="0 0 8 8"><path d="M1 4l2 2 4-4" stroke="#9dbdba" fill="none" stroke-width="1.2"/></svg></span><div><div class="list-title">Schlaf &amp; Stress</div><div class="copy" style="color:var(--muted)">Ausgleich für das Nervensystem und erholsamer Schlaf.</div></div></div>
      <div class="list-item"><span class="list-icon"><svg width="8" height="8" viewBox="0 0 8 8"><path d="M1 4l2 2 4-4" stroke="#9dbdba" fill="none" stroke-width="1.2"/></svg></span><div><div class="list-title">Stoffwechsel</div><div class="copy" style="color:var(--muted)">Aktivierung des Kreislaufs und Unterstützung beim Gewichtsmanagement.</div></div></div>
      <div class="list-item"><span class="list-icon"><svg width="8" height="8" viewBox="0 0 8 8"><path d="M1 4l2 2 4-4" stroke="#9dbdba" fill="none" stroke-width="1.2"/></svg></span><div><div class="list-title">Immunsystem</div><div class="copy" style="color:var(--muted)">Regelmäßige Anwendungen stärken die natürlichen Abwehrkräfte.</div></div></div>
    </div>
    <div style="position:absolute;left:0;right:0;bottom:14px;text-align:center;font-size:6.5px;font-weight:600;color:var(--teal-light)">www.velmarin.at</div>
  </div>

  <div class="panel dark">
    <div style="position:absolute;left:22px;top:26px;width:212px">
      <h2 class="heading" style="color:var(--teal-light);margin-bottom:10px">Preise | Pakete</h2>
      <div class="price-row"><span>Einzelanwendung</span><b>€ 45,–</b></div>
      <div class="price-row"><span>Schnupperpaket 3 Anwendungen</span><b>€ 125,–</b></div>
      <div class="price-row"><span>5er-Karte</span><b>€ 205,–</b></div>
      <div class="price-row"><span>10er-Karte Kurbehandlung</span><b>€ 390,–</b></div>
      <div class="price-row"><span>Sportlerpaket Saison</span><b>€ 590,–</b></div>
      <div class="price-row"><span>Vereinspaket ab 5 Personen</span><b>auf Anfrage</b></div>
      <div class="price-row"><span>Gutschein Einzelanwendung</span><b>€ 45,–</b></div>
      <div class="copy" style="margin-top:10px;color:var(--muted)">Alle Preise inkl. MwSt. Karten sind personenbezogen und zwölf Monate gültig. Termine nach Vereinbarung.</div>
      <div style="margin-top:14px;display:flex;align-items:center;gap:8px">
        <span style="width:30px;height:30px;background:var(--white);display:block"></span>
        <span class="copy" style="color:var(--muted)">Jetzt Termin sichern unter<br><b style="color:var(--white)">www.velmarin.at</b></span>
      </div>
    </div>
    <svg style="position:absolute;left:0;top:330px" width="257" height="40" viewBox="0 0 257 40">
      <path d="M0 40 C90 0 170 30 257 6 L257 40 Z" fill="var(--teal-light)"/>
    </svg>
    <div class="photo" role="img" aria-label="Foto: Schwimmer im Wasser" style="left:0;top:368px;width:257px;height:184px;background:linear-gradient(180deg,#7fa6bd,#2f5a78)"></div>
  </div>
</section>

</body>
</html>
```